Personal Trainer and Corporate Health Business

I need a business card for a new company I'm starting in Australia called "Brisk Vitality Partners" I will be providing a Personal training service as well as corporate health in companies.
The service provided is to help promote an active and healthy lifstyle.
The design should communicate a healthy lifestyle and also the benefits that this can have on a personal level and in the corporate environment and the benefits that flow from that.

Target Market(s)

Members of the public and Corporate

Industry/Entity Type

Environment

Requirements
Must have
• Company logo attached
Look and feel fresh and modern

Tag line: "Actively promoting a healthier lifestyle"

Lewis Norgate
Managing Director

m: 0417 596 304
e: lewis@briskvitalitypartners.com.au

www.briskvitalitypartners.com.au
Nice to have
• Can be 1 or 2 sided

```html
<!DOCTYPE html>
<html lang="en">
<head>
<meta charset="utf-8">
<title>Brisk Vitality Partners – Business Card</title>
<link href="https://fonts.googleapis.com/css2?family=Exo+2:wght@400;600&display=swap" rel="stylesheet">
<style>
  :root {
    --brand-blue: #1f6cc0;
    --brand-green: #a8cd3a;
    --card-white: #ffffff;
    --stage: #2e2e30;
    --text-light: #ffffff;
  }
  * { margin: 0; padding: 0; box-sizing: border-box; }
  html, body { width: 1200px; height: 720px; overflow: hidden; }
  body {
    background: var(--stage);
    font-family: "Exo 2", Arial, sans-serif;
    display: flex;
    align-items: center;
    justify-content: center;
    gap: 40px;
  }
  .card {
    position: relative;
    width: 540px;
    height: 308px;
    background: var(--card-white);
    overflow: hidden;
    box-shadow: 0 10px 30px rgba(0,0,0,.45);
  }

  /* Front */
  .front-panel {
    position: absolute;
    left: 0; right: 0; bottom: 0;
    height: 178px;
    background: var(--brand-blue);
    border-top: 3px solid var(--brand-green);
  }
  .front-panel::before {
    content: "";
    position: absolute;
    left: 0; right: 0; top: 4px;
    border-top: 1.5px dashed rgba(255,255,255,.8);
  }
  .brand {
    position: absolute;
    display: flex;
    align-items: center;
    gap: 9px;
  }
  .brand-dot {
    width: 18px; height: 18px;
    border-radius: 50%;
    background: var(--brand-green);
    flex: none;
  }
  .brand-name {
    color: var(--brand-blue);
    font-weight: 600;
    font-size: 24px;
    letter-spacing: .3px;
    white-space: nowrap;
  }
  .front .brand { left: 36px; top: 66px; }

  .person {
    position: absolute;
    left: 40px; bottom: 46px;
  }
  .person-name {
    color: var(--brand-green);
    font-size: 27px;
    font-weight: 400;
    line-height: 1.1;
  }
  .person-role {
    color: var(--text-light);
    font-size: 11px;
    margin-top: 5px;
  }

  .contact-list {
    position: absolute;
    left: 282px; top: 24px;
    list-style: none;
    color: var(--text-light);
    font-size: 11px;
  }
  .contact-list li {
    display: flex;
    align-items: center;
    gap: 8px;
    height: 18px;
    margin-bottom: 3px;
  }
  .contact-list svg { width: 12px; height: 12px; flex: none; }
  .contact-list .no-icon { padding-left: 0; }

  /* Back */
  .back {
    background: linear-gradient(to bottom,
      var(--brand-blue) 0 28%,
      var(--card-white) 28% 72%,
      var(--brand-blue) 72% 100%);
  }
  .back .brand {
    left: 50%; top: 50%;
    transform: translate(-50%, -50%);
  }
  .tagline {
    position: absolute;
    left: 0; right: 0; top: 178px;
    text-align: center;
    color: var(--brand-green);
    font-size: 11px;
    letter-spacing: 2px;
    text-transform: uppercase;
  }
</style>
</head>
<body>

  <section class="card front" aria-label="Business card front">
    <div class="brand">
      <span class="brand-dot"></span>
      <span class="brand-name">Brisk Vitality Partners</span>
    </div>

    <div class="front-panel">
      <ul class="contact-list">
        <li>
          <svg viewBox="0 0 24 24" aria-hidden="true"><path fill="#a8cd3a" d="M6.6 10.8a15 15 0 0 0 6.6 6.6l2.2-2.2a1 1 0 0 1 1-.25 11.4 11.4 0 0 0 3.6.57 1 1 0 0 1 1 1V20a1 1 0 0 1-1 1A17 17 0 0 1 3 4a1 1 0 0 1 1-1h3.5a1 1 0 0 1 1 1c0 1.25.2 2.45.57 3.57a1 1 0 0 1-.25 1z"/></svg>
          0417 596 304
        </li>
        <li>
          <svg viewBox="0 0 24 24" aria-hidden="true"><path fill="#a8cd3a" d="M2 5h20v14H2z"/><path fill="none" stroke="#1f6cc0" stroke-width="2" d="M2 5l10 8 10-8"/></svg>
          lewis@briskvitalitypartners.com.au
        </li>
        <li>
          <svg viewBox="0 0 24 24" aria-hidden="true"><circle cx="12" cy="12" r="9" fill="none" stroke="#a8cd3a" stroke-width="2.5"/><path fill="none" stroke="#a8cd3a" stroke-width="2" d="M3 12h18M12 3c3 3 3 15 0 18M12 3c-3 3-3 15 0 18"/></svg>
          www.briskvitalitypartners.com.au
        </li>
        <li class="no-icon">48 Tallow Rd Elsternwick, VIC 3185</li>
      </ul>

      <div class="person">
        <p class="person-name">Lewis Norgate</p>
        <p class="person-role">Managing Director</p>
      </div>
    </div>
  </section>

  <section class="card back" aria-label="Business card back">
    <div class="brand">
      <span class="brand-dot"></span>
      <span class="brand-name">Brisk Vitality Partners</span>
    </div>
  </section>

</body>
</html>
```